Bookmark Design

We would like to design a book mark with logos of our two business and a quote.

One side with the quote "The first wealth is health" - Tobias Quill Harrow and the two logos.

The back side has the two logos with its respective phone numbers and a common address (this is to be advised to the winner of the project).

```html
<!DOCTYPE html>
<html lang="en">
<head>
<meta charset="utf-8">
<title>Bookmark Design – Front and Back</title>
<link href="https://fonts.googleapis.com/css2?family=Montserrat:wght@400;500;600&family=Poppins:wght@500;600&display=swap" rel="stylesheet">
<style>
  :root {
    --backdrop: #b8b8b8;
    --navy: #1a2a55;
    --navy-deep: #0b0d45;
    --ocean: #06305f;
    --lime: #8cc63f;
    --icon-green: #62b946;
    --white: #ffffff;
  }
  * { margin: 0; padding: 0; box-sizing: border-box; }
  html, body { width: 1038px; height: 1200px; overflow: hidden; }
  body {
    background: var(--backdrop);
    position: relative;
    font-family: "Montserrat", sans-serif;
    color: var(--white);
  }
  .bookmark {
    position: absolute;
    top: 100px;
    width: 357px;
    height: 1003px;
    overflow: hidden;
    box-shadow: 0 6px 18px rgba(0,0,0,0.35);
  }
  .bookmark--front {
    left: 110px;
    background:
      radial-gradient(ellipse 260px 200px at 0% 140px, rgba(38,146,90,0.95), transparent 70%),
      radial-gradient(ellipse 300px 160px at 100% 660px, rgba(31,127,90,0.95), transparent 70%),
      radial-gradient(ellipse 380px 180px at 20% 600px, rgba(20,90,75,0.7), transparent 70%),
      linear-gradient(180deg, #1c4a56 0%, #0a2a3f 30%, #04193a 42%, #0c1848 75%, var(--navy) 100%);
  }
  .bookmark--back {
    left: 565px;
    background:
      radial-gradient(ellipse 300px 200px at 40% 60px, rgba(34,140,95,0.95), transparent 75%),
      radial-gradient(ellipse 260px 200px at 0% 560px, rgba(20,95,100,0.6), transparent 70%),
      radial-gradient(ellipse 380px 220px at 50% 980px, rgba(6,48,96,1), transparent 80%),
      linear-gradient(180deg, #16516a 0%, #0a2e55 30%, #061c46 55%, var(--navy-deep) 72%, var(--ocean) 100%);
  }
  .hang-hole {
    position: absolute;
    left: 160px;
    top: 69px;
    width: 36px;
    height: 36px;
    border-radius: 50%;
    background: var(--white);
    box-shadow: inset 0 2px 3px rgba(0,0,0,0.35);
  }
  .decor-area {
    position: absolute;
    left: 168px;
    top: 8px;
    width: 189px;
    height: 400px;
    background: linear-gradient(160deg, rgba(60,120,150,0.35), rgba(40,55,150,0.55) 40%, rgba(25,45,110,0.25) 80%, transparent);
    -webkit-mask-image: linear-gradient(90deg, transparent, #000 35%), linear-gradient(180deg, #000 70%, transparent);
    -webkit-mask-composite: source-in;
    mask-image: linear-gradient(90deg, transparent, #000 35%), linear-gradient(180deg, #000 70%, transparent);
    mask-composite: intersect;
  }
  .quote {
    position: absolute;
    left: 0;
    width: 100%;
    top: 392px;
    text-align: center;
    font-family: "Poppins", sans-serif;
    font-weight: 500;
    font-size: 61px;
    line-height: 61px;
    text-shadow: 0 3px 4px rgba(0,0,0,0.55);
  }
  .quote-author {
    position: absolute;
    left: 0;
    width: 100%;
    top: 610px;
    text-align: center;
    font-size: 24px;
    font-weight: 400;
    text-shadow: 0 2px 3px rgba(0,0,0,0.5);
  }
  .brand {
    position: absolute;
    left: 0;
    width: 100%;
    display: flex;
    flex-direction: column;
    align-items: center;
    justify-content: center;
    font-family: "Poppins", sans-serif;
    font-weight: 600;
    color: var(--lime);
    line-height: 1.1;
    text-align: center;
  }
  .brand-mark {
    border-radius: 50%;
    background: var(--lime);
    margin-bottom: 10px;
  }
  .front .brand--clinic { top: 705px; height: 136px; font-size: 26px; }
  .front .brand--clinic .brand-mark { width: 72px; height: 72px; }
  .front .brand--dental { top: 858px; height: 96px; font-size: 24px; }
  .front .brand--dental .brand-mark { width: 44px; height: 44px; margin-bottom: 8px; }
  .back .brand--clinic { top: 225px; height: 172px; font-size: 30px; }
  .back .brand--clinic .brand-mark { width: 104px; height: 104px; margin-bottom: 12px; }
  .back .brand--dental { top: 418px; height: 118px; font-size: 28px; }
  .back .brand--dental .brand-mark { width: 60px; height: 60px; }
  .contact-icon {
    position: absolute;
    left: 147px;
    width: 58px;
    height: 58px;
    border-radius: 50%;
    background: var(--icon-green);
    display: flex;
    align-items: center;
    justify-content: center;
  }
  .contact-icon--phone { top: 598px; }
  .contact-icon--pin { top: 749px; }
  .phone-number {
    position: absolute;
    left: 0; width: 100%;
    top: 664px;
    text-align: center;
    font-family: "Poppins", sans-serif;
    font-weight: 500;
    font-size: 34px;
    text-shadow: 0 2px 3px rgba(0,0,0,0.5);
  }
  .address {
    position: absolute;
    left: 0; width: 100%;
    top: 820px;
    text-align: center;
    font-size: 18px;
    font-weight: 500;
    line-height: 23px;
    text-shadow: 0 2px 3px rgba(0,0,0,0.5);
  }
</style>
</head>
<body>
  <section class="bookmark bookmark--front front">
    <div class="decor-area" role="img" aria-label="Large soft leaf decoration in blue and green"></div>
    <div class="hang-hole"></div>
    <h1 class="quote">The First<br>wealth is<br>Health</h1>
    <p class="quote-author">Tobias Quill Harrow</p>
    <div class="brand brand--clinic"><span class="brand-mark"></span>Fernbrook Clinic</div>
    <div class="brand brand--dental"><span class="brand-mark"></span>Harbourline Dental</div>
  </section>

  <section class="bookmark bookmark--back back">
    <div class="hang-hole"></div>
    <div class="brand brand--clinic"><span class="brand-mark"></span>Fernbrook Clinic</div>
    <div class="brand brand--dental"><span class="brand-mark"></span>Harbourline Dental</div>

    <div class="contact-icon contact-icon--phone">
      <svg width="34" height="34" viewBox="0 0 24 24" aria-hidden="true">
        <path d="M6.6 3.5l2.6 3.2c.4.5.4 1.2-.1 1.7L7.8 9.7c1.2 2.6 3.9 5.3 6.5 6.5l1.3-1.3c.5-.5 1.2-.5 1.7-.1l3.2 2.6c.5.4.6 1.2.1 1.7l-1.6 1.6c-.8.8-2 1.1-3.1.7C9.9 19.5 4.5 14.1 2.6 8.1c-.4-1.1-.1-2.3.7-3.1l1.6-1.6c.5-.5 1.3-.4 1.7.1z" fill="none" stroke="#fff" stroke-width="1.6" stroke-linejoin="round"/>
      </svg>
    </div>
    <p class="phone-number">001-5550-2714</p>

    <div class="contact-icon contact-icon--pin">
      <svg width="30" height="34" viewBox="0 0 24 28" aria-hidden="true">
        <path d="M12 1.5C6.8 1.5 3 5.3 3 10.2c0 6 9 16.3 9 16.3s9-10.3 9-16.3c0-4.9-3.8-8.7-9-8.7z" fill="#fff"/>
        <circle cx="12" cy="10" r="3.6" fill="none" stroke="#62b946" stroke-width="1.8"/>
      </svg>
    </div>
    <p class="address">Lorem ipsum dolor sit amet,<br>consectetur</p>
  </section>
</body>
</html>
```